Lodging Venture Advisors

I am an independent operator engaged on short/medium term consultancy briefs within the Hotel/Resort sector in the Pacific Area and have a representation in Fiji.

A broad based services is offered and includes:

Development Advisory
Property Management
Sales & Marketing
Holiday Ownership/Timeshare
Resorts/Apartments/Motels/Flashpackers/B&B
Financial & Legal Referrals

Industry/Entity Type

Hotel

Contact Information for Business Card

Business name - LODGING VENTURE ADVISORS
My name - Grant Whitlock
Address: PO Box 382 Coral Heights 4219 Qld
Phone: Australia: +61 7 55904283 Mobile: 0418952064 (Viber)
Fiji: +679 8527319
Email: grantmwhitlock@netmailbox.example

```html
<!DOCTYPE html>
<html lang="en">
<head>
<meta charset="utf-8">
<title>Lodging Venture Advisors – Business Card</title>
<link rel="stylesheet" href="https://fonts.googleapis.com/css2?family=Michroma&family=Roboto:wght@400;700&display=swap">
<style>
  :root {
    --bg: #d6d6d6;
    --ink: #0b0b0b;
    --paper: #f1f1f1;
    --paper-shade: #e4e4e4;
    --title: #e2e2e2;
    --ring: #9a9a9a;
    --text: #1c1c1c;
    --white: #ffffff;
  }
  * { box-sizing: border-box; margin: 0; padding: 0; }
  html, body { width: 1200px; height: 900px; overflow: hidden; }
  body {
    background: var(--bg);
    font-family: "Roboto", Arial, sans-serif;
    position: relative;
  }
  .card {
    position: absolute;
    left: 270px;
    width: 660px;
    height: 380px;
    background: linear-gradient(180deg, var(--paper), var(--paper-shade));
    box-shadow: 0 10px 24px rgba(0,0,0,.28);
    overflow: hidden;
  }
  .card--contact { top: 50px; }
  .card--services { top: 470px; }
  .card__band {
    position: absolute;
    left: 0; top: 0;
    width: 100%;
    height: 170px;
    background: var(--ink);
  }
  .card__mark {
    position: absolute;
    left: 36px;
    top: 106px;
    width: 128px;
    height: 128px;
    border-radius: 50%;
    background: var(--ink);
    border: 5px solid var(--ring);
  }
  .card__title {
    position: absolute;
    right: 40px;
    top: 108px;
    font-family: "Michroma", Arial, sans-serif;
    font-weight: 400;
    font-size: 25px;
    line-height: 28px;
    color: var(--title);
    letter-spacing: 1px;
    text-align: right;
  }
  .card__title span { display: block; }
  .card__title .line-2 { margin-right: 120px; }
  .card__holder {
    position: absolute;
    right: 30px;
    top: 22px;
    font-weight: 700;
    font-size: 15px;
    color: var(--white);
    letter-spacing: .5px;
  }
  .contact {
    position: absolute;
    display: flex;
    flex-direction: column;
    gap: 10px;
    font-size: 14px;
    color: var(--text);
  }
  .contact--left { left: 190px; top: 262px; }
  .contact--right { left: 372px; top: 196px; }
  .contact__item { display: flex; align-items: center; gap: 8px; white-space: nowrap; }
  .contact__icon { width: 20px; height: 20px; flex: none; }
  .contact__address {
    position: absolute;
    left: 330px;
    top: 322px;
    font-size: 14px;
    color: var(--text);
    white-space: nowrap;
  }
  .services {
    position: absolute;
    left: 0; right: 0;
    top: 260px;
    text-align: center;
    font-size: 15px;
    line-height: 19px;
    letter-spacing: 1.2px;
    color: var(--text);
  }
</style>
</head>
<body>

<section class="card card--contact" aria-label="Business card front">
  <div class="card__band"></div>
  <p class="card__holder">GRANT WHITLOCK</p>
  <h1 class="card__title"><span>LODGING VENTURE</span><span class="line-2">ADVISORS</span></h1>
  <div class="card__mark" aria-hidden="true"></div>

  <div class="contact contact--right">
    <div class="contact__item">
      <svg class="contact__icon" viewBox="0 0 20 20" aria-hidden="true"><circle cx="10" cy="10" r="10" fill="#0b0b0b"/><rect x="7" y="4.5" width="6" height="11" rx="1" fill="#fff"/><rect x="8" y="6" width="4" height="6" fill="#0b0b0b"/></svg>
      <span>+679 8527319 (Viber - Fiji)</span>
    </div>
    <div class="contact__item">
      <svg class="contact__icon" viewBox="0 0 20 20" aria-hidden="true"><circle cx="10" cy="10" r="10" fill="#0b0b0b"/><rect x="4.5" y="6.5" width="11" height="7.5" fill="#fff"/><path d="M4.5 6.5 L10 11 L15.5 6.5" fill="none" stroke="#0b0b0b" stroke-width="1"/></svg>
      <span>grantmwhitlock@netmailbox.example</span>
    </div>
  </div>

  <div class="contact contact--left">
    <div class="contact__item">
      <svg class="contact__icon" viewBox="0 0 20 20" aria-hidden="true"><circle cx="10" cy="10" r="10" fill="#0b0b0b"/><rect x="7" y="4.5" width="6" height="11" rx="1" fill="#fff"/><rect x="8" y="6" width="4" height="6" fill="#0b0b0b"/></svg>
      <span>0418952064</span>
    </div>
    <div class="contact__item">
      <svg class="contact__icon" viewBox="0 0 20 20" aria-hidden="true"><circle cx="10" cy="10" r="10" fill="#0b0b0b"/><path d="M6.5 5 L8.5 5 L9.5 7.8 L8.2 9 C9 10.7 9.6 11.3 11 11.9 L12.2 10.6 L15 11.6 L15 13.6 C15 14.4 14.4 15 13.6 15 C9.4 14.7 5.3 10.6 5 6.4 C5 5.6 5.6 5 6.5 5 Z" fill="#fff"/></svg>
      <span>+61 7 55904283 (Australia)</span>
    </div>
  </div>

  <p class="contact__address">PO Box 382 Coral Heights 4219 Qld</p>
</section>

<section class="card card--services" aria-label="Business card back">
  <div class="card__band"></div>
  <h2 class="card__title"><span>LODGING VENTURE</span><span class="line-2">ADVISORS</span></h2>
  <div class="card__mark" aria-hidden="true"></div>
  <p class="services">
    Development Advisory | Project/Site/Property Management | Sales &amp; Marketing |<br>
    Holiday Ownership/Timeshare | Resorts/Hotels/Apartments/Motels |<br>
    Financial &amp; Legal Referrals
  </p>
</section>

</body>
</html>
```